VMR business card

Need a business card for a company that provides instructional design and elearning development services. The website is here: http://vantmoro.studio/

I'm attaching a current logo, as well as the old business card design. While I like to keep it clean, the old design is too simplistic for my liking. The only idea I want to reuse from the old design is placing industry jargon on the back of the card, just need a better way to present it. But if you have other ideas for the back--feel free to experiment.

Please use the colors complementary to the color we have on the website. Thank you!

```html
<!DOCTYPE html>
<html lang="en">
<head>
<meta charset="utf-8">
<title>VMR business card</title>
<link href="https://fonts.googleapis.com/css2?family=Lato:wght@700&family=Open+Sans:wght@400;600&display=swap" rel="stylesheet">
<style>
  :root {
    --teal: #12b0b0;
    --sand: #d9cb8d;
    --ink: #333333;
    --card: #ffffff;
    --backdrop: #e9e6e1;
  }
  html, body {
    margin: 0;
    width: 1200px;
    height: 1000px;
    overflow: hidden;
    background: var(--backdrop);
  }
  .card {
    position: absolute;
    left: 265px;
    width: 665px;
    height: 397px;
    background: var(--card);
    border-radius: 26px;
    overflow: hidden;
    box-shadow: 0 6px 14px rgba(0,0,0,0.18);
    font-family: "Open Sans", Arial, sans-serif;
    color: var(--ink);
  }
  .card--front { top: 73px; }
  .card--back { top: 533px; }

  .wordmark {
    position: absolute;
    margin: 0;
    font-family: "Open Sans", Arial, sans-serif;
    font-weight: 600;
    color: var(--teal);
    letter-spacing: 2px;
    line-height: 1;
  }
  .card--front .wordmark { left: 33px; top: 52px; font-size: 58px; }
  .card--back .wordmark { left: 0; right: 0; top: 70px; text-align: center; font-size: 66px; }

  .holder-name {
    position: absolute;
    left: 33px;
    top: 213px;
    margin: 0;
    font-family: "Lato", Arial, sans-serif;
    font-weight: 700;
    font-size: 20px;
    color: var(--teal);
  }
  .contact-list {
    position: absolute;
    left: 33px;
    top: 266px;
    margin: 0;
    padding: 0;
    list-style: none;
    font-size: 16px;
  }
  .contact-list li {
    display: flex;
    align-items: center;
    height: 25.5px;
  }
  .contact-list svg { width: 16px; height: 16px; margin-right: 7px; fill: var(--teal); }

  .front-band {
    position: absolute;
    left: 0;
    bottom: 0;
    width: 665px;
    height: 18px;
    background: linear-gradient(90deg, var(--teal) 0%, var(--teal) 50%, var(--sand) 72%, var(--teal) 100%);
  }

  .services {
    position: absolute;
    left: 0;
    top: 213px;
    width: 665px;
    margin: 0;
    padding: 0;
    list-style: none;
  }
  .service {
    position: absolute;
    width: 160px;
    text-align: center;
    transform: translateX(-50%);
  }
  .service__badge {
    width: 84px;
    height: 84px;
    margin: 0 auto;
    box-sizing: border-box;
    border: 2px solid var(--teal);
    border-radius: 50%;
    display: flex;
    align-items: center;
    justify-content: center;
  }
  .service__badge svg { width: 44px; height: 44px; fill: var(--sand); }
  .service__label {
    margin-top: 20px;
    font-size: 16px;
    line-height: 22px;
    text-transform: uppercase;
  }
</style>
</head>
<body>

<section class="card card--front" aria-label="Card front">
  <p class="wordmark">VMR</p>
  <h1 class="holder-name">Dorian Kessler</h1>
  <ul class="contact-list">
    <li><svg viewBox="0 0 16 16"><path d="M1 6c0-2 3-3 7-3s7 1 7 3v1h-3V5.5H4V7H1z M3 8h10l1 6H2z"/></svg>555-014-2286</li>
    <li><svg viewBox="0 0 16 16"><path d="M1 3h14v10H1z" fill="var(--teal)"/><path d="M1 3l7 6 7-6" fill="none" stroke="#fff" stroke-width="1.4"/></svg>dkessler@vantmoro.studio</li>
    <li><svg viewBox="0 0 16 16"><circle cx="8" cy="8" r="6.5" fill="none" stroke="var(--teal)" stroke-width="2"/><path d="M4 6h8M4 10h8M8 1.5v13" stroke="var(--teal)" stroke-width="1.2"/></svg>www.vantmoro.studio</li>
  </ul>
  <div class="front-band" role="img" aria-label="Decorative teal and sand footer band"></div>
</section>

<section class="card card--back" aria-label="Card back">
  <p class="wordmark">VMR</p>
  <ul class="services">
    <li class="service" style="left:123px">
      <div class="service__badge"><svg viewBox="0 0 44 44"><path d="M8 14h9a5 5 0 1 1 8 0h9v9a5 5 0 1 0 0 8v9H25a5 5 0 1 0-8 0H8z"/></svg></div>
      <div class="service__label">Instructional<br>Design</div>
    </li>
    <li class="service" style="left:266px">
      <div class="service__badge"><svg viewBox="0 0 44 44"><path d="M7 10h24v14a8 8 0 0 1-8 8h-8a8 8 0 0 1-8-8z"/><path d="M31 13h3a5 5 0 0 1 0 10h-3" fill="none" stroke="var(--sand)" stroke-width="3"/><rect x="4" y="35" width="34" height="3" rx="1.5"/></svg></div>
      <div class="service__label">eLearning<br>Development</div>
    </li>
    <li class="service" style="left:405px">
      <div class="service__badge"><svg viewBox="0 0 44 44"><path d="M12 34a9 9 0 0 1-1-18 11 11 0 0 1 21 2 8 8 0 0 1 0 16z"/><path d="M22 17v11M17 24l5 5 5-5" fill="none" stroke="#fff" stroke-width="3"/></svg></div>
      <div class="service__label">Mobile<br>Learning</div>
    </li>
    <li class="service" style="left:543px">
      <div class="service__badge"><svg viewBox="0 0 44 44"><path d="M6 14h8l3-4h10l3 4h8v20H6z"/><circle cx="22" cy="24" r="6" fill="#fff"/><circle cx="22" cy="24" r="3.5"/></svg></div>
      <div class="service__label">Insructor-led<br>Training</div>
    </li>
  </ul>
</section>

</body>
</html>
```